Lakeshore Skyburst Website Design

I am looking for a website design ( Home page and inner template page ) in a .psd format. The home page needs to have a large hero image what will function as a "slider", and have some highlight graphical areas/links to the following links "Public & Municipal Events", "Corporate Events", "Special Events". The main navigation needs to have the following nav links "gallery", "home", "about", "services" and "contact". Unfortunately the client does not have any nice hi-rez images ( this is a company that specializes is large fireworks displays ) so please use stock photography sample images from plainframes since we have an account there an can purchase the photos if our client wants to use them. Our current full time graphic artist has been with us for a long time so we are looking at sketchforum as a way to add a fresh approach to design and possibly find someone we can work with regularly. Here is a few designs that in the way we display them for our clients for approval. As you can see there are a couple that don't have their own images so they are utilizing the before mentioned plainframes samples. On the plus side we did manage to get their logo in a .ai format. We have our team for handling the conversion from design to html.

http://quillbarnstudio.example/dev/

```html
<!DOCTYPE html>
<html lang="en">
<head>
<meta charset="utf-8">
<title>Lakeshore Skyburst</title>
<link rel="stylesheet" href="https://fonts.googleapis.com/css2?family=Lora:wght@700&family=Roboto:wght@400;500;700&display=swap">
<style>
:root{
  --accent:#4aa3dc;
  --ink:#111;
  --body:#666;
  --night:#1a1650;
  --band:#3f8fc8;
  --footer:#3b3b3b;
  --line:#e6e6e6;
}
*{box-sizing:border-box;margin:0;padding:0}
html,body{width:1200px;height:2757px;overflow:hidden;background:#fff}
body{position:relative;font-family:'Roboto',sans-serif;color:var(--ink)}
.abs{position:absolute}
.serif{font-family:'Lora',serif;font-weight:700}

.site-header{left:0;top:0;width:1200px;height:76px;background:#fff;z-index:3}
.brand{left:111px;top:0;width:171px;height:110px;background:#fff;z-index:4;display:flex;align-items:center;justify-content:center;gap:8px}
.brand-dot{width:12px;height:12px;border-radius:50%;background:var(--accent)}
.brand-name{font-family:'Roboto',sans-serif;font-weight:500;font-size:17px;color:#333}
.main-nav{left:410px;top:30px;z-index:5;display:flex;gap:29px;font-size:14px;font-weight:500;letter-spacing:.2px;line-height:17px}
.main-nav a{color:#222;text-decoration:none}
.main-nav a.current{color:var(--accent)}
.header-phone{left:882px;top:22px;z-index:5;display:flex;align-items:center;gap:14px;font-size:25px;font-weight:500;color:#111}

.hero{left:0;top:76px;width:1200px;height:618px;background:radial-gradient(ellipse at 50% 35%,#5a3fa8 0%,#2a2270 40%,#14104a 80%)}
.hero-band{left:0;top:520px;width:1200px;height:174px;background:rgba(30,24,80,.55)}
.hero-title{left:158px;top:556px;font-size:39px;color:#fff}
.hero-text{left:158px;top:611px;width:590px;font-size:15px;line-height:22px;color:#fff}
.btn{display:flex;align-items:center;justify-content:center;gap:12px;font-weight:500;color:#fff;font-size:16px;letter-spacing:.3px}
.hero-btn{left:863px;top:582px;width:178px;height:50px;background:var(--accent);border-radius:3px}

.section-title{width:1200px;left:0;text-align:center;font-size:36px;line-height:44px}
.card-img{width:315px;height:203px;box-shadow:0 0 0 3px #fff,0 0 6px 3px rgba(0,0,0,.12)}
.card-title{font-size:14px;font-weight:500;letter-spacing:.2px}
.card-rule{width:30px;height:2px;background:var(--accent)}
.card-text{width:280px;font-size:15px;line-height:24px;color:var(--body)}
.card-link{font-size:14px;font-weight:500;color:var(--accent);text-decoration:underline;display:flex;align-items:center;gap:8px}

.divider{left:0;top:1368px;width:1200px;height:1px;background:var(--line)}

.contact-band{left:0;top:2124px;width:1200px;height:587px;background:radial-gradient(ellipse at 50% 50%,#5aa7db 0%,#3f8fc8 60%,#3580bd 100%)}
.contact-title{left:0;top:2190px;width:1200px;text-align:center;font-size:42px;color:#fff}
.contact-text{left:250px;top:2260px;width:700px;text-align:center;font-size:15px;line-height:22px;color:#fff}
.info-icon{width:50px;height:50px;border-radius:50%;background:#fff;display:flex;align-items:center;justify-content:center}
.info-label{font-size:15px;font-weight:500;color:#fff}
.info-value{font-size:15px;line-height:22px;color:#fff}
.field{background:#fff;height:48px;width:317px;display:flex;align-items:center;justify-content:space-between;padding:0 20px;font-size:15px;color:#777}
.field-message{left:781px;top:2384px;width:316px;height:168px;align-items:flex-start;padding-top:16px}
.submit{left:781px;top:2564px;width:163px;height:48px;background:#9aa3ab;font-size:15px}
.site-footer{left:0;top:2711px;width:1200px;height:46px;background:var(--footer);color:#fff;font-size:15px;display:flex;align-items:center;justify-content:center}
</style>
</head>
<body>

<header class="abs site-header"></header>
<div class="abs brand"><span class="brand-dot"></span><span class="brand-name">Lakeshore Skyburst</span></div>
<nav class="abs main-nav">
  <a class="current" href="#">HOME</a><a href="#">ABOUT</a><a href="#">SERVICES</a><a href="#">GALLERY</a><a href="#">CONTACT</a>
</nav>
<div class="abs header-phone">
  <svg width="32" height="32" viewBox="0 0 32 32"><circle cx="16" cy="16" r="16" fill="#4aa3dc"/><path d="M11 9c1-1 2 0 3 2s0 2-1 3c1 2 3 4 5 5 1-1 1-2 3-1s3 2 2 3c-1 2-3 3-6 1-3-2-6-5-7-8-1-3 0-4 1-5z" fill="#fff"/></svg>
  <span>1 555 010 2040</span>
</div>

<section class="abs hero" role="img" aria-label="Colourful fireworks bursting across a night sky"></section>
<div class="abs hero-band"></div>
<h1 class="abs serif hero-title">Lakeshore Skyburst</h1>
<p class="abs hero-text">At vero eos et accusamus et iusto odio dignissimos ducimus qui blanditiis praesentium voluptatum deleniti atque corrupti</p>
<a class="abs btn hero-btn">GET STARTED
  <svg width="16" height="16" viewBox="0 0 16 16"><circle cx="8" cy="8" r="8" fill="#fff"/><path d="M5 8h6M8 5l3 3-3 3" stroke="#4aa3dc" stroke-width="2" fill="none"/></svg></a>

<h2 class="abs serif section-title" style="top:788px">Lakeshore Skyburst<br>for Your Event</h2>

<div class="abs card-img" style="left:108px;top:921px;background:radial-gradient(circle at 50% 30%,#c7844a,#5a2a1a 60%,#2a120c)" role="img" aria-label="Golden fireworks over a bokeh background"></div>
<div class="abs card-img" style="left:443px;top:921px;background:radial-gradient(circle at 33% 55%,#f0a040,#3a5a7c 35%,#1d3a5c)" role="img" aria-label="Sparkler glowing against a blue dusk"></div>
<div class="abs card-img" style="left:777px;top:921px;background:radial-gradient(circle at 55% 25%,#e8e0c8,#7a6a4a 35%,#2a2218)" role="img" aria-label="Crowd watching white fireworks"></div>

<h3 class="abs card-title" style="left:131px;top:1148px">PUBLIC &amp; MUNICIPAL EVENTS</h3>
<h3 class="abs card-title" style="left:466px;top:1148px">CORPORATE EVENTS</h3>
<h3 class="abs card-title" style="left:800px;top:1148px">SPECIAL EVENTS</h3>
<div class="abs card-rule" style="left:131px;top:1175px"></div>
<div class="abs card-rule" style="left:466px;top:1175px"></div>
<div class="abs card-rule" style="left:800px;top:1175px"></div>
<p class="abs card-text" style="left:131px;top:1187px">Lorem ipsum dolor sit amet, consectetur adipiscing elit, sed do eiusmod tempor incididunt ut labore et dolor</p>
<p class="abs card-text" style="left:466px;top:1187px">Lorem ipsum dolor sit amet, consectetur adipiscing elit, sed do eiusmod tempor incididunt ut labore et dolor</p>
<p class="abs card-text" style="left:800px;top:1187px">Lorem ipsum dolor sit amet, consectetur adipiscing elit, sed do eiusmod tempor incididunt ut labore et dolor</p>
<a class="abs card-link" style="left:132px;top:1269px">LEARN MORE <svg width="13" height="13" viewBox="0 0 16 16"><circle cx="8" cy="8" r="8" fill="#4aa3dc"/><path d="M5 8h6M8 5l3 3-3 3" stroke="#fff" stroke-width="2" fill="none"/></svg></a>
<a class="abs card-link" style="left:467px;top:1269px">LEARN MORE <svg width="13" height="13" viewBox="0 0 16 16"><circle cx="8" cy="8" r="8" fill="#4aa3dc"/><path d="M5 8h6M8 5l3 3-3 3" stroke="#fff" stroke-width="2" fill="none"/></svg></a>
<a class="abs card-link" style="left:801px;top:1269px">LEARN MORE <svg width="13" height="13" viewBox="0 0 16 16"><circle cx="8" cy="8" r="8" fill="#4aa3dc"/><path d="M5 8h6M8 5l3 3-3 3" stroke="#fff" stroke-width="2" fill="none"/></svg></a>

<div class="abs divider"></div>

<h2 class="abs serif section-title" style="top:1421px">Latest From Minnesota</h2>

<div class="abs" style="left:115px;top:1516px;width:237px;height:182px;background:linear-gradient(135deg,#c04ab0,#4a1a5a)" role="img" aria-label="Celebrating figure under pink fireworks"></div>
<div class="abs" style="left:115px;top:1706px;width:237px;height:277px;background:linear-gradient(180deg,#3a2a3a,#8a6a8a 60%,#3a3040)" role="img" aria-label="Fireworks over a city skyline"></div>
<div class="abs" style="left:359px;top:1516px;width:237px;height:276px;background:linear-gradient(160deg,#2a2a8a,#7a4ac0 55%,#1a1a3a)" role="img" aria-label="Blue and purple fireworks over a crowd"></div>
<div class="abs" style="left:359px;top:1801px;width:237px;height:182px;background:linear-gradient(160deg,#c08040,#3a2418 70%)" role="img" aria-label="Orange fireworks above spectators"></div>
<div class="abs" style="left:604px;top:1516px;width:237px;height:182px;background:radial-gradient(circle at 50% 40%,#e0a070,#2a2238 55%)" role="img" aria-label="People watching fireworks at night"></div>
<div class="abs" style="left:604px;top:1706px;width:237px;height:277px;background:linear-gradient(180deg,#5a6a7a,#1e2632)" role="img" aria-label="Crowd raising hands under white fireworks"></div>
<div class="abs" style="left:848px;top:1516px;width:237px;height:276px;background:linear-gradient(180deg,#3a4a5a,#8a6a5a 60%,#3a2a2a)" role="img" aria-label="Friends celebrating with confetti at dusk"></div>
<div class="abs" style="left:848px;top:1801px;width:237px;height:182px;background:radial-gradient(circle at 45% 50%,#b05a4a,#2a1e22 65%)" role="img" aria-label="Red and white fireworks over silhouettes"></div>

<section class="abs contact-band"></section>
<h2 class="abs serif contact-title">Contact us</h2>
<p class="abs contact-text">Sed ut perspiciatis unde omnis iste natus error sit voluptatem accusantium doloremque laudantium, totam rem aperiam, eaque ipsa quae ab illo inventore veritatis et quasi architecto beatae</p>

<div class="abs info-icon" style="left:111px;top:2403px"><svg width="24" height="24" viewBox="0 0 24 24"><path d="M12 2a7 7 0 0 0-7 7c0 5 7 13 7 13s7-8 7-13a7 7 0 0 0-7-7z" fill="none" stroke="#4aa3dc" stroke-width="1.5"/><circle cx="12" cy="9" r="2.5" fill="none" stroke="#4aa3dc" stroke-width="1.5"/></svg></div>
<div class="abs info-label" style="left:185px;top:2399px">LOCATION</div>
<div class="abs info-value" style="left:185px;top:2424px">48 Harbor Point Rd,<br>United States</div>

<div class="abs info-icon" style="left:111px;top:2498px"><svg width="24" height="24" viewBox="0 0 24 24"><rect x="3" y="6" width="18" height="13" fill="none" stroke="#4aa3dc" stroke-width="1.5"/><path d="M3 6l9 7 9-7" fill="none" stroke="#4aa3dc" stroke-width="1.5"/></svg></div>
<div class="abs info-label" style="left:185px;top:2498px">EMAIL US</div>
<div class="abs info-value" style="left:185px;top:2523px">info@lakeshoreskyburst.example</div>

<div class="abs info-icon" style="left:111px;top:2570px"><svg width="24" height="24" viewBox="0 0 24 24"><path d="M7 3c1-1 2 0 3 2s0 3-1 4c1 2 3 4 5 5 1-1 2-2 4-1s3 2 2 3c-1 3-4 4-7 2-4-2-7-6-8-9-1-3 1-5 2-6z" fill="none" stroke="#4aa3dc" stroke-width="1.5"/></svg></div>
<div class="abs info-label" style="left:185px;top:2571px">CONTACT US</div>
<div class="abs info-value" style="left:185px;top:2596px">1 555 010 2040</div>

<div class="abs field" style="left:440px;top:2384px">First Name <svg width="14" height="14" viewBox="0 0 14 14"><circle cx="7" cy="7" r="6" fill="none" stroke="#666"/><circle cx="7" cy="5.5" r="2" fill="#666"/><path d="M3.5 11a4 3 0 0 1 7 0" fill="#666"/></svg></div>
<div class="abs field" style="left:440px;top:2444px">Email <svg width="14" height="12" viewBox="0 0 14 12"><rect x="1" y="1" width="12" height="10" fill="none" stroke="#666"/><path d="M1 1l6 5 6-5" fill="none" stroke="#666"/></svg></div>
<div class="abs field" style="left:440px;top:2504px">Phone No <svg width="12" height="12" viewBox="0 0 12 12"><path d="M2 1c1 0 2 2 2 3l-1 1c1 2 2 3 4 4l1-1c1 0 3 1 3 2s-1 2-2 2C5 12 0 7 0 3 0 2 1 1 2 1z" fill="#666"/></svg></div>
<div class="abs field" style="left:440px;top:2564px">Post Code <svg width="10" height="14" viewBox="0 0 10 14"><path d="M5 1a4 4 0 0 0-4 4c0 3 4 8 4 8s4-5 4-8a4 4 0 0 0-4-4z" fill="#666"/><circle cx="5" cy="5" r="1.5" fill="#fff"/></svg></div>
<div class="abs field field-message">Message <svg width="14" height="12" viewBox="0 0 14 12"><ellipse cx="6" cy="5" rx="5" ry="4" fill="none" stroke="#666"/><path d="M3 8l-1 3 3-2" fill="#666"/></svg></div>
<a class="abs btn submit">SUBMIT NOW <svg width="14" height="14" viewBox="0 0 16 16"><circle cx="8" cy="8" r="8" fill="#fff"/><path d="M5 8h6M8 5l3 3-3 3" stroke="#9aa3ab" stroke-width="2" fill="none"/></svg></a>

<footer class="abs site-footer">© 2021 Lakeshore Skyburst. All Rights Reserved</footer>

</body>
</html>
```